Business Card Design for Software Development Company

I am looking for a business card design the incorporates my new logo (attached below).

Key information to include:
Name: Darnell Whisket
Title: CEO
Email: darnell@brovatecore.com
Phone: 418-926-7301
Website: www.brovatecore.com

NOTE: This design should be easy to edit so that we can order cards for different members of our team.

```html
<!DOCTYPE html>
<html lang="en">
<head>
<meta charset="utf-8">
<title>BrovateCore Business Cards</title>
<link href="https://fonts.googleapis.com/css2?family=Montserrat:wght@300;400;700&display=swap" rel="stylesheet">
<style>
  :root {
    --bg: #d9d8d4;
    --card: #ffffff;
    --navy: #343a52;
    --teal: #17b39c;
    --orange: #e97f22;
    --ink: #343a52;
  }
  * { box-sizing: border-box; margin: 0; padding: 0; }
  html, body { width: 1200px; height: 801px; overflow: hidden; }
  body {
    background: var(--bg);
    font-family: "Montserrat", sans-serif;
    color: var(--ink);
    position: relative;
  }
  .card {
    position: absolute;
    top: 246px;
    width: 540px;
    height: 309px;
    background: var(--card);
    border-bottom: 3px solid var(--teal);
    box-shadow: 0 8px 24px rgba(0,0,0,0.18);
    overflow: hidden;
  }
  .card--front { left: 40px; }
  .card--back { left: 620px; }

  .brand { position: absolute; display: flex; align-items: center; gap: 14px; }
  .brand__mark { border-radius: 50%; background: var(--orange); flex: none; }
  .brand__name { font-weight: 700; color: var(--navy); letter-spacing: -0.5px; line-height: 1; }
  .brand__tagline {
    position: absolute; font-weight: 700; color: var(--navy);
    text-transform: uppercase; letter-spacing: 0.6px; white-space: nowrap;
  }

  .card--front .brand { left: 40px; top: 48px; }
  .card--front .brand__mark { width: 34px; height: 34px; }
  .card--front .brand__name { font-size: 52px; }
  .card--front .brand__tagline { left: 334px; top: 108px; font-size: 8px; }

  .person { position: absolute; left: 40px; top: 178px; }
  .person__name { font-size: 25px; font-weight: 700; color: var(--teal); letter-spacing: 0.3px; white-space: nowrap; }
  .person__title { font-size: 15px; font-weight: 400; margin-top: 4px; text-align: right; }

  .divider { position: absolute; left: 272px; top: 150px; width: 2px; height: 58px; background: var(--teal); }

  .contact { position: absolute; left: 292px; top: 138px; list-style: none; }
  .contact__item { display: flex; align-items: center; gap: 8px; font-size: 14px; font-weight: 400; line-height: 26px; white-space: nowrap; }
  .contact__icon { width: 13px; height: 13px; flex: none; }

  .band {
    position: absolute; left: 0; right: 0; bottom: 0; height: 20px;
    background: var(--teal);
  }

  .card--back .brand { left: 50%; top: 50%; transform: translate(-50%, -60%); }
  .card--back .brand__mark { width: 38px; height: 38px; }
  .card--back .brand__name { font-size: 58px; }
  .card--back .brand__tagline { left: 317px; top: 192px; font-size: 9px; }
</style>
</head>
<body>

<section class="card card--front" aria-label="Business card front">
  <div class="brand">
    <span class="brand__mark"></span>
    <span class="brand__name">BrovateCore</span>
  </div>
  <p class="brand__tagline">A division of Brovate Group</p>

  <div class="person">
    <p class="person__name">Darnell Whisket</p>
    <p class="person__title">CEO</p>
  </div>

  <span class="divider"></span>

  <ul class="contact">
    <li class="contact__item">
      <svg class="contact__icon" viewBox="0 0 16 16"><path fill="#17b39c" d="M3.6 1.5l2.3 2.3-1.3 1.9a9 9 0 0 0 5.7 5.7l1.9-1.3 2.3 2.3-1.7 2.1C7.6 14.3 1.7 8.4 1.5 3.2z"/></svg>
      418-926-7301
    </li>
    <li class="contact__item">
      <svg class="contact__icon" viewBox="0 0 16 16"><rect x="1" y="3" width="14" height="10" rx="1" fill="#17b39c"/><path d="M1.5 4l6.5 5 6.5-5" fill="none" stroke="#fff" stroke-width="1.3"/></svg>
      darnell@brovatecore.com
    </li>
    <li class="contact__item">
      <svg class="contact__icon" viewBox="0 0 16 16"><circle cx="8" cy="8" r="7" fill="#17b39c"/><path d="M1 8h14M8 1c-3 3.5-3 10.5 0 14M8 1c3 3.5 3 10.5 0 14" fill="none" stroke="#fff" stroke-width="1"/></svg>
      www.brovatecore.com
    </li>
  </ul>

  <div class="band" role="img" aria-label="Decorative brand colour band along the bottom edge"></div>
</section>

<section class="card card--back" aria-label="Business card back">
  <div class="brand">
    <span class="brand__mark"></span>
    <span class="brand__name">BrovateCore</span>
  </div>
  <p class="brand__tagline">A division of Brovate Group</p>
</section>

</body>
</html>
```